"Coastline Motor Traders" business that imports classic cars, motorbikes and boats from the USA needs a bus

We need a business card design for our new company based in Brisbane Australia called "Coastline Motor Traders". You designed our company logo which I have attached. We source and import American Classic, Muscle and Vintage cars for customers in Australia. We also do the same for motor bikes and we will eventually move into boats. The logo is a very strong one so we feel that the colours of the card can not detract from the logo but enhance it. The font needs to be professional but not boring. We are finding dream machines for people so it needs to feel strong and safe, yet fun and be very cool.

Industry/Entity Type

Business

Contact Information for Business Card

Martin Kelloway

Brisbane, QLD
Australia
Mobile: +61417 562 304
Email: martin kelloway@mailbox-example.com

Requirements
Must have
• Strong logo presence
• Identify what we do
Should not have
• don't want it to be cluttered with text

```html
<!DOCTYPE html>
<html lang="en">
<head>
<meta charset="utf-8">
<title>Coastline Motor Traders – Business Card</title>
<link rel="stylesheet" href="https://fonts.googleapis.com/css2?family=Sorts+Mill+Goudy&display=swap">
<style>
  :root {
    --page: #ffffff;
    --navy-deep: #16344f;
    --navy-light: #245a7e;
    --red: #c8112e;
    --red-deep: #b20d27;
    --red-soft: #e0404f;
    --cream: #f6d7c8;
    --white: #ffffff;
    --shadow: rgba(0, 0, 0, 0.22);
  }
  * { margin: 0; padding: 0; box-sizing: border-box; }
  html, body {
    width: 1200px;
    height: 665px;
    overflow: hidden;
    background: var(--page);
    font-family: "Sorts Mill Goudy", Georgia, serif;
  }
  .card {
    position: absolute;
    top: 111px;
    width: 312px;
    height: 444px;
    overflow: hidden;
    background: var(--red);
    box-shadow: 2px 3px 6px var(--shadow);
  }
  .card--front { left: 222px; }
  .card--back { left: 669px; }

  .star-band {
    position: absolute;
    left: 0; top: 0;
    width: 100%;
    height: 126px;
    background: radial-gradient(ellipse at 50% 80%, var(--navy-light) 0%, var(--navy-deep) 75%);
  }
  .ray-field {
    position: absolute;
    left: 0; top: 126px;
    width: 100%;
    height: 318px;
    background: radial-gradient(ellipse at 50% 0%, var(--red-deep) 0%, var(--red) 40%, var(--red-soft) 100%);
  }

  .brand {
    position: absolute;
    left: 14px; top: 160px;
    width: 284px;
    padding: 18px 10px 20px;
    border-radius: 18px;
    background: var(--navy-deep);
    display: flex;
    flex-direction: column;
    align-items: center;
    text-align: center;
    color: var(--white);
  }
  .brand__mark {
    width: 52px;
    height: 52px;
    border-radius: 50%;
    background: var(--cream);
    margin-bottom: 10px;
  }
  .brand__name {
    font-size: 38px;
    line-height: 1.05;
    font-weight: 400;
    color: var(--white);
  }
  .brand__tagline {
    margin-top: 12px;
    font-size: 15px;
    line-height: 1.2;
    letter-spacing: 0.04em;
    color: var(--cream);
  }

  .contact {
    position: absolute;
    left: 0; top: 220px;
    width: 100%;
    text-align: center;
    color: var(--white);
  }
  .contact__name {
    font-size: 30px;
    font-weight: 400;
    line-height: 1;
    margin-bottom: 27px;
  }
  .contact__line {
    font-size: 18.5px;
    line-height: 27.5px;
  }
  .contact__line--email { font-size: 15px; }
</style>
</head>
<body>
  <section class="card card--front">
    <div class="star-band" role="img" aria-label="Navy field scattered with white stars"></div>
    <div class="ray-field" role="img" aria-label="Red and white sunburst rays radiating from the star band"></div>
    <div class="brand">
      <span class="brand__mark"></span>
      <h1 class="brand__name">Coastline<br>Motor Traders</h1>
      <p class="brand__tagline">American classic cars · motorbikes · boats</p>
    </div>
  </section>

  <section class="card card--back">
    <div class="star-band" role="img" aria-label="Navy field scattered with white stars"></div>
    <div class="contact">
      <h2 class="contact__name">Martin Kelloway</h2>
      <p class="contact__line">Brisbane, QLD</p>
      <p class="contact__line">Australia</p>
      <p class="contact__line">Mobile: +61417 562 304</p>
      <p class="contact__line contact__line--email">Email: martin kelloway@mailbox-example.com</p>
    </div>
  </section>
</body>
</html>
```